Labels for essential oils small botlles

We are Slovenia based company Velnira Botanic Ltd. www.velnira-botanic.com We offer essential oils as pure essential oils or blends (mixed) essential oils. We have different kind of essential oils 40+ and blends. We sell in different sizes as: 10ml, 30ml, 50ml and 100ml. But majority is 10ml.
All essential oils are in glass bottles with closer. We will now change bottles style from amber to cobalt blue with black closure (see picture attached)
We would like to have different stile of label for different category of essential oils. Here is link about different categories of essential oils https://www.vialquarry.com/mixing-guides/ . The different style / color could be by note:
- Top notes
- Middle notes
- Base notes
- Mixes – different oils mixed together and named as chill out, deep breath, sleep well, etc
Possible is also differentiation regarding:
• Citrus
• Floral
• Herbaceous
• Camphoraceous
• Spicy
• Resinous
• Woody
• Earthy
• Mixes

On labels should be also pictograms according to REACH directive of EU and label according to CPL (see attached file). We would also like to add EAN code attached on the edge of the label. On label is some text fixed I try to show in pdf attached file and some is variable depends from essential oil and date of production.

Meaning we need general labels for each note or other classification and one for mixes – you could also show your option or classification on something else with story behind.

10 ml roll 30 mm x 70 mm (1,25”x3”) but finial dimensions will follow.

We use Tessaro Qm700 printer. For editing labels we use BarTender which support also EAN codes. We import labels as picture in background or different according to your instructions.

Target Market(s)

Retail, health and wellness, all audiences and web shop

Industry/Entity Type

Health And Wellness

Font styles to use
Other font styles liked:
• GillLigHr is our font but could be different

Colors

Designer to choose colors to be used in the design.

Requirements
Must have
• Label should be as template that we could use for different oils in same group. More in attached document. According to CLP we have to put red pictograms on labels which is not nice and should be some how nicely integrated. on the edge EAB dar code that products could be sell through online.
Nice to have
• Different colours, some symbol as a drop or flower or herb. Logo is not necessary that is on label. We would like that label it self represent our brand.

```html
<!DOCTYPE html>
<html lang="sl">
<head>
<meta charset="utf-8">
<title>Velnira Botanic – essential oil labels</title>
<link href="https://fonts.googleapis.com/css2?family=Cabin+Condensed:wght@400;600;700&family=Lato:wght@400;700;900&family=Lobster&display=swap" rel="stylesheet">
<style>
  :root{
    --backdrop:#657674;
    --face:#070707;
    --ink:#ffffff;
    --hazard:#e0202a;
    --code-area:#f4f4f4;
    --pine:#f4a23a; --pine-2:#f6cf3a;
    --melisa:#e8418f; --melisa-2:#e88fbf;
    --relax:#8cc63f; --relax-2:#a7d65a;
    --sleep:#1e86c8; --sleep-2:#2fa6df;
    --drop:#f3d12f; --drop-2:#fbe98a;
  }
  *{box-sizing:border-box;margin:0;padding:0}
  html,body{width:1200px;height:720px;overflow:hidden;background:var(--backdrop)}
  body{position:relative;font-family:"Cabin Condensed","Lato",sans-serif;color:var(--ink)}
  .sheet{position:absolute;inset:0}

  .label{position:absolute;width:572px;height:250px;
    background:linear-gradient(90deg,var(--accent),var(--accent-2) 50%,var(--accent));
    box-shadow:0 4px 0 rgba(0,0,0,.35)}
  .label--pine{left:16px;top:86px;--accent:var(--pine);--accent-2:var(--pine-2)}
  .label--melisa{left:610px;top:86px;--accent:var(--melisa);--accent-2:var(--melisa-2)}
  .label--relax{left:16px;top:382px;--accent:var(--relax);--accent-2:var(--relax-2)}
  .label--sleep{left:610px;top:382px;--accent:var(--sleep);--accent-2:var(--sleep-2)}

  .face{position:absolute;inset:6px 12px;background:var(--face)}

  .panel{position:absolute;top:4px;height:224px;border:2px solid var(--accent);border-radius:18px;overflow:hidden}
  .hazards{left:10px;width:180px}
  .warning{left:398px;width:140px;padding:4px 6px 0 7px}

  .pictogram{position:absolute;left:6px;width:36px;height:36px}
  .pictogram:nth-of-type(1){top:8px}
  .pictogram:nth-of-type(2){top:42px}
  .pictogram:nth-of-type(3){top:76px}
  .pictogram:nth-of-type(4){top:112px}

  .fact{position:absolute;left:54px;font-size:12px;line-height:13px}
  .fact b{display:block;font-family:"Lato",sans-serif;font-weight:900;font-size:10.5px;letter-spacing:.2px}
  .fact--substances{top:12px}
  .fact--serial{top:64px}
  .fact--expiry{top:116px}

  .ean-area{position:absolute;left:12px;top:152px;width:42px;height:64px;background:var(--code-area)}
  .maker{position:absolute;left:62px;top:154px;font-size:11.8px;line-height:13.2px}

  .warning h3{font-family:"Cabin Condensed",sans-serif;font-size:18px;font-weight:600;line-height:20px;margin-bottom:1px}
  .warning p{font-size:10.8px;line-height:12.9px}

  .feature{position:absolute;left:204px;width:180px;top:0;height:238px;text-align:center;font-family:"Lato",sans-serif}
  .feature::before,.feature::after{content:"";position:absolute;top:42px;bottom:16px;width:1px;background:var(--accent)}
  .feature::before{left:2px}
  .feature::after{right:2px}
  .arc{position:absolute;left:0;top:4px;width:180px;height:60px}
  .arc text{font:400 13px "Lato",sans-serif;fill:var(--ink);letter-spacing:.5px}
  .drop-art{position:absolute;left:66px;top:30px;width:58px;height:58px;
    border-radius:50% 0 50% 50%;transform:rotate(-45deg);
    background:radial-gradient(circle at 40% 60%,var(--drop-2),var(--drop) 70%)}
  .name{position:absolute;left:0;right:0;top:112px;font-size:17px;font-weight:700;letter-spacing:.3px}
  .script{position:absolute;left:0;right:0;font-family:"Lobster",cursive;font-size:29px;color:var(--accent);line-height:32px}
  .script--under{top:130px}
  .script--solo{top:112px}
  .dots{position:absolute;left:0;right:0;font-size:9px;color:var(--accent);letter-spacing:2px}
  .dots--under{top:164px}
  .dots--solo{top:146px}
  .latin{position:absolute;left:0;right:0;font-family:"Cabin Condensed",sans-serif;font-size:12px;line-height:13px}
  .latin--under{top:180px}
  .latin--solo{top:160px}
  .brand{position:absolute;left:0;right:0;bottom:6px;font-size:18px;font-weight:700;letter-spacing:.3px}
</style>
</head>
<body>
<svg width="0" height="0" style="position:absolute" aria-hidden="true">
  <defs>
    <symbol id="diamond" viewBox="0 0 40 40">
      <rect x="7" y="7" width="26" height="26" transform="rotate(45 20 20)" fill="#fff" stroke="#e0202a" stroke-width="3.5"/>
    </symbol>
    <symbol id="ghs-exclamation" viewBox="0 0 40 40">
      <use href="#diamond"/>
      <rect x="18" y="10" width="4" height="14" rx="1.5" fill="#000"/>
      <circle cx="20" cy="28.5" r="2.4" fill="#000"/>
    </symbol>
    <symbol id="ghs-environment" viewBox="0 0 40 40">
      <use href="#diamond"/>
      <path d="M11 28h18M15 28v-12M15 18l-3-3M15 20l3-3M22 26c2-3 6-3 8 0c-2 2-6 2-8 0z" stroke="#000" stroke-width="2" fill="none"/>
    </symbol>
    <symbol id="ghs-flame" viewBox="0 0 40 40">
      <use href="#diamond"/>
      <path d="M20 9c3 5 7 8 7 13a7 7 0 0 1-14 0c0-3 2-5 3-7c1 3 2 4 3 4c1-3 0-6 1-10z" fill="#000"/>
      <rect x="12" y="29" width="16" height="2" fill="#000"/>
    </symbol>
    <symbol id="ghs-health" viewBox="0 0 40 40">
      <use href="#diamond"/>
      <circle cx="20" cy="13" r="3" fill="#000"/>
      <path d="M13 30c0-8 3-12 7-12s7 4 7 12z" fill="#000"/>
      <path d="M20 20l-3 4l3 4l3-4z" fill="#fff"/>
    </symbol>
    <path id="arc-path" d="M14 62 A80 62 0 0 1 166 62"/>
  </defs>
</svg>

<main class="sheet">

  <article class="label label--pine">
    <div class="face">
      <section class="panel hazards">
        <svg class="pictogram"><use href="#ghs-exclamation"/></svg>
        <svg class="pictogram"><use href="#ghs-environment"/></svg>
        <svg class="pictogram"><use href="#ghs-flame"/></svg>
        <svg class="pictogram"><use href="#ghs-health"/></svg>
        <p class="fact fact--substances"><b>NEVARNE SNOVI</b>1,8 cimeol, geraniol</p>
        <p class="fact fact--serial"><b>SERIJSKA ŠTEVILKA</b>15-600-001277</p>
        <p class="fact fact--expiry"><b>ROK UPORABE</b>09 / 2016</p>
        <div class="ean-area" role="img" aria-label="Space for the EAN code"></div>
        <p class="maker">VSEBINA 10ml<br>Velnira Botanic d.o.o.,<br>Brezova ulica 27,<br>SI-1000 Ljubljana<br>T 014200517</p>
      </section>
      <section class="feature">
        <svg class="arc" viewBox="0 0 180 60"><text><textPath href="#arc-path" startOffset="50%" text-anchor="middle">100% PURE ESSENTIAL OIL</textPath></text></svg>
        <div class="drop-art" role="img" aria-label="Yellow oil drop with a green herb sprig"></div>
        <h2 class="name">SREBRNA JELKA</h2>
        <p class="script script--under">Pine Oil</p>
        <p class="dots dots--under">• ● •</p>
        <p class="latin latin--under">PINUS NIGRA<br>TWIG LEAFOIL</p>
        <p class="brand">Velnira Botanic</p>
      </section>
      <section class="panel warning">
        <h3>NEVARNO</h3>
        <p>Povzroča draženje kože. Lahko povzroči alergijski odziv kože. Povzroča hude poškodbe oči. Strupeno za vodne organizme, z dolgotrajnimi učinki. Ne vdihavati prahu, dima, plina, meglice, hlapov razpršila. Nositi zaščitne rokavice/ obleko, zaščito za obraz in oči.Ibere simenda ndaepel mi, quam, testBus dit rehenem</p>
      </section>
    </div>
  </article>

  <article class="label label--melisa">
    <div class="face">
      <section class="panel hazards">
        <svg class="pictogram"><use href="#ghs-exclamation"/></svg>
        <svg class="pictogram"><use href="#ghs-environment"/></svg>
        <svg class="pictogram"><use href="#ghs-flame"/></svg>
        <svg class="pictogram"><use href="#ghs-health"/></svg>
        <p class="fact fact--substances"><b>NEVARNE SNOVI</b>1,8 cimeol, geraniol</p>
        <p class="fact fact--serial"><b>SERIJSKA ŠTEVILKA</b>15-600-001277</p>
        <p class="fact fact--expiry"><b>ROK UPORABE</b>09 / 2016</p>
        <div class="ean-area" role="img" aria-label="Space for the EAN code"></div>
        <p class="maker">VSEBINA 10ml<br>Velnira Botanic d.o.o.,<br>Brezova ulica 27,<br>SI-1000 Ljubljana<br>T 014200517</p>
      </section>
      <section class="feature">
        <svg class="arc" viewBox="0 0 180 60"><text><textPath href="#arc-path" startOffset="50%" text-anchor="middle">100% PURE ESSENTIAL OIL</textPath></text></svg>
        <div class="drop-art" role="img" aria-label="Yellow oil drop with a green herb sprig"></div>
        <h2 class="name">MELISA</h2>
        <p class="script script--under">Melisa Oil</p>
        <p class="dots dots--under">• ● •</p>
        <p class="latin latin--under">CYMBOPOGON<br>WINTERIANUS</p>
        <p class="brand">Velnira Botanic</p>
      </section>
      <section class="panel warning">
        <h3>NEVARNO</h3>
        <p>Povzroča draženje kože. Lahko povzroči alergijski odziv kože. Povzroča hude poškodbe oči. Strupeno za vodne organizme, z dolgotrajnimi učinki. Ne vdihavati prahu, dima, plina, meglice, hlapov razpršila. Nositi zaščitne rokavice/ obleko, zaščito za obraz in oči.Ibere simenda ndaepel mi, quam, testBus dit rehenem</p>
      </section>
    </div>
  </article>

  <article class="label label--relax">
    <div class="face">
      <section class="panel hazards">
        <svg class="pictogram"><use href="#ghs-exclamation"/></svg>
        <svg class="pictogram"><use href="#ghs-environment"/></svg>
        <svg class="pictogram"><use href="#ghs-flame"/></svg>
        <svg class="pictogram"><use href="#ghs-health"/></svg>
        <p class="fact fact--substances"><b>NEVARNE SNOVI</b>1,8 cimeol, geraniol</p>
        <p class="fact fact--serial"><b>SERIJSKA ŠTEVILKA</b>15-600-001277</p>
        <p class="fact fact--expiry"><b>ROK UPORABE</b>09 / 2016</p>
        <div class="ean-area" role="img" aria-label="Space for the EAN code"></div>
        <p class="maker">VSEBINA 10ml<br>Velnira Botanic d.o.o.,<br>Brezova ulica 27,<br>SI-1000 Ljubljana<br>T 014200517</p>
      </section>
      <section class="feature">
        <svg class="arc" viewBox="0 0 180 60"><text><textPath href="#arc-path" startOffset="50%" text-anchor="middle">100% PURE ESSENTIAL OIL</textPath></text></svg>
        <div class="drop-art" role="img" aria-label="Yellow oil drop with a green herb sprig"></div>
        <p class="script script--solo">Relaxing</p>
        <p class="dots dots--solo">• ● •</p>
        <p class="latin latin--solo">CHILIQUEM ACIENTRA<br>HAC TAM DETI, UTUROXL<br>MIHILICUSI PERFEX<br>SENTUSQUA VAST RE INATRE</p>
        <p class="brand">Velnira Botanic</p>
      </section>
      <section class="panel warning">
        <h3>NEVARNO</h3>
        <p>Povzroča draženje kože. Lahko povzroči alergijski odziv kože. Povzroča hude poškodbe oči. Strupeno za vodne organizme, z dolgotrajnimi učinki. Ne vdihavati prahu, dima, plina, meglice, hlapov razpršila. Nositi zaščitne rokavice/ obleko, zaščito za obraz in oči.Ibere simenda ndaepel mi, quam, testBus dit rehenem</p>
      </section>
    </div>
  </article>

  <article class="label label--sleep">
    <div class="face">
      <section class="panel hazards">
        <svg class="pictogram"><use href="#ghs-exclamation"/></svg>
        <svg class="pictogram"><use href="#ghs-environment"/></svg>
        <svg class="pictogram"><use href="#ghs-flame"/></svg>
        <svg class="pictogram"><use href="#ghs-health"/></svg>
        <p class="fact fact--substances"><b>NEVARNE SNOVI</b>1,8 cimeol, geraniol</p>
        <p class="fact fact--serial"><b>SERIJSKA ŠTEVILKA</b>15-600-001277</p>
        <p class="fact fact--expiry"><b>ROK UPORABE</b>09 / 2016</p>
        <div class="ean-area" role="img" aria-label="Space for the EAN code"></div>
        <p class="maker">VSEBINA 10ml<br>Velnira Botanic d.o.o.,<br>Brezova ulica 27,<br>SI-1000 Ljubljana<br>T 014200517</p>
      </section>
      <section class="feature">
        <svg class="arc" viewBox="0 0 180 60"><text><textPath href="#arc-path" startOffset="50%" text-anchor="middle">100% PURE ESSENTIAL OIL</textPath></text></svg>
        <div class="drop-art" role="img" aria-label="Yellow oil drop with a green herb sprig"></div>
        <p class="script script--solo">Sleep Well</p>
        <p class="dots dots--solo">• ● •</p>
        <p class="latin latin--solo">CHILIQUEM ACIENTRA<br>HAC TAM DETI, UTUROXL<br>MIHILICUSI PERFEX<br>SENTUSQUA VAST RE INATRE</p>
        <p class="brand">Velnira Botanic</p>
      </section>
      <section class="panel warning">
        <h3>NEVARNO</h3>
        <p>Povzroča draženje kože. Lahko povzroči alergijski odziv kože. Povzroča hude poškodbe oči. Strupeno za vodne organizme, z dolgotrajnimi učinki. Ne vdihavati prahu, dima, plina, meglice, hlapov razpršila. Nositi zaščitne rokavice/ obleko, zaščito za obraz in oči.Ibere simenda ndaepel mi, quam, testBus dit rehenem</p>
      </section>
    </div>
  </article>

</main>
</body>
</html>
```